New Zealand Luggage Importer Needs Business Cards

We need professional, creative and fashionable business cards created.
We are based in New Zealand and import and distribute high-end, quality, fashionable and durable luggage.
We pride ourselves on selling the very best quality luggage, second only to 1 brand (which we won't mention here)...we use the same manufacturer. However, our prices are much more reasonable.
Industry/Entity Type
Business
Contact Information for Business Card
Mark Dunsley
027 512 4068
3/17 Harlow Street, Pinecrest Flats, Auckland, 0614
PO Box 204377, Fernside, Auckland 0731
09-528-3916
sales@brivancases.co.nz / www.brivancases.co.nz

```html
<!DOCTYPE html>
<html lang="en">
<head>
<meta charset="utf-8">
<title>Brivan Cases – Business Cards</title>
<link rel="stylesheet" href="https://fonts.googleapis.com/css2?family=Open+Sans:wght@400;600;700&display=swap">
<style>
  :root {
    --page-bg: #e9e7e4;
    --card-black: #231f20;
    --gold-dark: #9c7630;
    --gold-mid: #c39a44;
    --gold-light: #f1d98a;
    --gold-text: #d1a94a;
    --white: #ffffff;
  }
  * { margin: 0; padding: 0; box-sizing: border-box; }
  html, body {
    width: 1200px;
    height: 780px;
    overflow: hidden;
    background: var(--page-bg);
    font-family: "Open Sans", Arial, sans-serif;
  }
  .sheet {
    width: 1200px;
    height: 780px;
    display: flex;
    align-items: center;
    justify-content: center;
    gap: 40px;
  }
  .card {
    width: 520px;
    height: 297px;
    padding: 13px;
    background: linear-gradient(120deg, var(--gold-dark) 0%, var(--gold-mid) 30%, var(--gold-light) 52%, var(--gold-mid) 70%, var(--gold-dark) 100%);
    box-shadow: 0 10px 24px rgba(0, 0, 0, 0.25);
  }
  .card-face {
    width: 100%;
    height: 100%;
    background: var(--card-black);
    position: relative;
    color: var(--white);
  }
  .wordmark {
    font-weight: 700;
    color: var(--white);
    letter-spacing: 0.04em;
    text-transform: uppercase;
    white-space: nowrap;
    line-height: 1;
  }
  /* Front */
  .card-front .wordmark {
    position: absolute;
    left: 92px;
    top: 102px;
    font-size: 36px;
  }
  .card-front .website {
    position: absolute;
    left: 96px;
    top: 156px;
    font-size: 11px;
    color: var(--gold-text);
  }
  /* Back */
  .card-back .wordmark {
    position: absolute;
    left: 118px;
    top: 64px;
    font-size: 36px;
  }
  .card-back .person-name {
    position: absolute;
    left: 0;
    right: 0;
    top: 132px;
    text-align: center;
    font-size: 17px;
    font-weight: 700;
  }
  .contact-list {
    position: absolute;
    left: 0;
    right: 0;
    top: 166px;
    list-style: none;
    text-align: center;
    font-size: 11px;
    line-height: 1.75;
  }
  .contact-label {
    color: var(--gold-text);
    font-weight: 600;
  }
</style>
</head>
<body>
  <main class="sheet">
    <section class="card card-front" aria-label="Business card front">
      <div class="card-face">
        <div class="wordmark">Brivan Cases</div>
        <div class="website">www.brivancases.co.nz</div>
      </div>
    </section>

    <section class="card card-back" aria-label="Business card back">
      <div class="card-face">
        <div class="wordmark">Brivan Cases</div>
        <div class="person-name">Mark Dunsley</div>
        <ul class="contact-list">
          <li><span class="contact-label">M:</span> 027 512 4068 | <span class="contact-label">P:</span> 09-528-3916 | <span class="contact-label">E:</span> sales@brivancases.co.nz</li>
          <li><span class="contact-label">A:</span> 3/17 Harlow Street, Pinecrest Flats, Auckland, 0614</li>
          <li><span class="contact-label">A:</span> PO Box 204377, Fernside, Auckland 0731</li>
        </ul>
      </div>
    </section>
  </main>
</body>
</html>
```